Trendy Indian Restaurant needs menu design

Menu takes inspiration from heron bowl and similar fast food qsr establishments.

Menu is to be for first print a vinyl. Size will be A1 horizontal. Need spanish menu as well.

I have included the menu details. Menu blue kettle hut 2 has some layout details. We really like how heron bowl has their menu and similar styles are appreciated. We do have 3 different entrees styles biriyani, combos, and kerala favorites.

Please use menu blue kettle hut 2 file as guide. the rest of the files are meant to be used for pricing and phrases.

Target Market(s)

hispanic shoppers, young professionals, low income shoppers, middle income

Industry/Entity Type

Indian Restaurant

Font styles to use
Serif
Sans Serif
Decorative

Colors

Designer to choose colors to be used in the design.

Requirements
Must have
• Menu with good placement of related materials.

```html
<!DOCTYPE html>
<html lang="en">
<head>
<meta charset="utf-8">
<title>Blue Kettle Hut Menu</title>
<link href="https://fonts.googleapis.com/css2?family=Signika:wght@400;600;700&display=swap" rel="stylesheet">
<style>
:root{
  --page:#e9e9e9;
  --cream:#fdebc0;
  --edge:#f3b44a;
  --lime:#d9dc1f;
  --lime-edge:#eec46a;
  --orange:#f05a28;
  --red:#c8202f;
  --maroon:#6e1c12;
  --ink:#2f2f2f;
  --white:#fffaf0;
}
*{box-sizing:border-box;margin:0;padding:0}
html,body{width:1200px;height:852px;overflow:hidden;background:var(--page);font-family:"Signika",sans-serif}
.menu{position:absolute;left:17px;top:13px;width:1166px;height:826px;background:var(--edge);box-shadow:0 2px 6px rgba(0,0,0,.35)}
.menu-inner{position:absolute;left:26px;top:25px;width:1114px;height:771px;background:var(--cream)}
.swirl{position:absolute;background:var(--orange);border-radius:50%}
.brand{position:absolute;left:0;width:100%;text-align:center;top:50px;font-weight:700;font-size:54px;color:var(--red);line-height:1}
.rule{position:absolute;left:51px;top:123px;width:1063px;height:10px;background:var(--orange);opacity:.75}
.panel{position:absolute;background:var(--lime);border:5px solid var(--lime-edge)}
.bar{position:absolute;background:var(--orange);color:var(--maroon);font-weight:600;font-size:17px;line-height:25px;text-align:center}
.bar.light{color:var(--white)}
.bar.left{text-align:left;padding-left:10px}
.row{position:absolute;font-size:16px;line-height:20px;color:var(--red);font-weight:600;white-space:nowrap}
.row.ink{color:var(--ink);font-weight:400;font-size:17px}
.price{position:absolute}
.note{position:absolute;font-size:8.5px;font-style:italic;line-height:10.5px;text-align:center;color:var(--ink)}
.dot::before{content:"•";position:absolute;left:-13px}
.prem{display:inline-block;background:var(--white);color:var(--ink);font-weight:600;padding:0 2px;line-height:17px}
.legend{position:absolute;left:430px;top:517px;width:315px;height:26px;background:var(--white);border:1px solid var(--orange);text-align:center;font-size:16px;line-height:24px;color:var(--ink);font-weight:600;letter-spacing:.5px}
</style>
</head>
<body>
<div class="menu">
 <div class="menu-inner"></div>

 <div class="swirl" style="left:136px;top:40px;width:239px;height:40px" role="img" aria-label="Decorative orange flourish"></div>
 <div class="swirl" style="left:788px;top:50px;width:239px;height:38px" role="img" aria-label="Decorative orange flourish"></div>
 <div class="brand">Blue Kettle Hut</div>
 <div class="rule" role="img" aria-label="Decorative bunting border"></div>

 <section class="panel" style="left:64px;top:147px;width:319px;height:398px"></section>
 <div class="bar light" style="left:69px;top:152px;width:309px;height:38px;font-size:22px;line-height:38px;font-weight:700">APPETIZER</div>
 <div class="row" style="left:81px;top:200px">Beef Puffs<span class="price" style="left:235px">$1</span></div>
 <div class="row" style="left:81px;top:220px">Chicken Puff<span class="price" style="left:235px">$1.5</span></div>
 <div class="row" style="left:81px;top:240px">Egg Puff<span class="price" style="left:235px">$2.25</span></div>
 <div class="row" style="left:81px;top:261px">Beff Cutlet<span class="price" style="left:235px">$1.5</span></div>
 <div class="row" style="left:81px;top:280px">Chicken Cutlet<span class="price" style="left:235px">$1.5</span></div>

 <div class="bar" style="left:69px;top:313px;width:309px">Biriyani</div>
 <div class="note" style="left:100px;top:342px;width:250px">Fragrant basmati rice cooked with cloves, cinnamon, cardamom, ginger and cashew nut then layered with curry, meat and baked to perfection. (Biryanis come with salad, poppadum, and pickle)</div>
 <div class="row" style="left:81px;top:392px">Chicken biriyani<span class="price" style="left:235px">$7</span></div>
 <div class="row" style="left:81px;top:413px">Goat biriyani<span class="price" style="left:235px">$10</span></div>

 <div class="bar" style="left:69px;top:445px;width:309px">Kerala Favorite Meal</div>
 <div class="row" style="left:81px;top:477px">Porotta and Beef Fry<span class="price" style="left:201px">$11</span></div>
 <div class="note" style="left:100px;top:497px;width:250px">Porotta a flaky buttery bread from Southern India is normally consumed with a Beef curry locally called 'Beef Fry'</div>

 <div class="bar light" style="left:430px;top:151px;width:315px">Step 1: Pick a Combo</div>
 <div class="row dot" style="left:461px;top:198px">1 Entrée Combo<span class="price" style="left:225px">$11</span></div>
 <div class="row dot" style="left:461px;top:218px">2 Curry Combo<span class="price" style="left:225px">$13</span></div>
 <div class="bar light" style="left:430px;top:268px;width:315px">Step 2: Pick Entrees</div>
 <div class="row" style="left:444px;top:320px;font-weight:400">Entrées</div>
 <div class="row ink dot" style="left:491px;top:347px">Chana Masala</div>
 <div class="row ink dot" style="left:491px;top:370px">Chicken Tikka Masala</div>
 <div class="row ink dot" style="left:491px;top:394px">Chicken 65</div>
 <div class="row ink dot" style="left:491px;top:417px">Chilli Chicken</div>
 <div class="row ink dot" style="left:491px;top:441px">Goat Curry <span class="prem">P</span> +$2.00</div>
 <div class="row ink dot" style="left:491px;top:464px">Beef Fry <span class="prem">P</span> +$1.00</div>
 <div class="legend"><span class="prem">P</span> = Premium items</div>

 <section class="panel" style="left:64px;top:560px;width:684px;height:219px"></section>
 <div class="bar left" style="left:66px;top:565px;width:316px">1.&nbsp;&nbsp; Appetizers Biriyani Kerala Fave</div>
 <div class="bar left" style="left:66px;top:632px;width:316px">2.&nbsp;&nbsp; Combo Menu</div>
 <div class="row" style="left:128px;top:670px;font-size:17px">o Step 1 choose a combo</div>
 <div class="row" style="left:128px;top:694px;font-size:17px">o Step 2 Choose an Entrée</div>
 <div class="row" style="left:128px;top:718px;font-size:17px">o Step three choose a side</div>
 <div class="row" style="left:144px;top:741px;font-size:17px">(naan, rice, chapptahi)</div>
 <div class="bar left" style="left:430px;top:634px;width:315px">3.&nbsp;&nbsp; Drinks and Dessert Addons</div>
 <div class="row" style="left:490px;top:671px;color:var(--maroon);font-weight:400;font-size:17px">(Rice, breads)</div>

 <section class="panel" style="left:792px;top:147px;width:325px;height:637px"></section>
 <div class="bar" style="left:797px;top:151px;width:315px">Meal EXTRAS</div>
 <div class="row dot" style="left:816px;top:221px">Extra Protein<span class="price" style="left:237px">$2.50</span></div>
 <div class="row dot" style="left:816px;top:244px">Poppadum and Pickle<span class="price" style="left:237px">$1</span></div>
 <div class="bar" style="left:797px;top:275px;width:315px">Drinks</div>
 <div class="row dot" style="left:816px;top:321px">Mango Juice<span class="price" style="left:237px">$2</span></div>
 <div class="row dot" style="left:816px;top:344px">Thunder Cola<span class="price" style="left:237px">$2</span></div>
 <div class="row dot" style="left:816px;top:368px">Ginger Beer<span class="price" style="left:237px">$2</span></div>
 <div class="row dot" style="left:816px;top:391px">Lychee Drink<span class="price" style="left:237px">$2</span></div>
 <div class="bar" style="left:797px;top:416px;width:315px">Extra Rice</div>
 <div class="row dot" style="left:816px;top:467px">Basmati Rice</div>
 <div class="row dot" style="left:816px;top:491px">Chicken Curry Rice<span class="price" style="left:237px">$2</span></div>
 <div class="bar" style="left:797px;top:515px;width:315px">Extra bread (Choose 1)</div>
 <div class="row dot" style="left:816px;top:562px">Chapatti</div>
 <div class="row dot" style="left:816px;top:586px">Naan<span class="price" style="left:237px">$1</span></div>
 <div class="row dot" style="left:816px;top:610px">Kerala Porotta<span class="price" style="left:237px">$1</span></div>
 <div class="bar" style="left:797px;top:632px;width:315px">Dessert</div>
 <div class="row dot" style="left:816px;top:682px">Mango Pudding</div>
 <div class="row dot" style="left:816px;top:705px">Rasmalai</div>
 <div class="row dot" style="left:816px;top:729px">Gulab Jamun</div>
 <div class="row dot" style="left:816px;top:752px">Rice Kheer</div>
</div>
</body>
</html>
```